Boutique hotel requires flyer for Tapas promotion

We need a flyer that will predominantly be used as a Face book promotion and for our website.
We would like to promote the fact that we offer Tapas & open our wine bar from 5pm to 8pm every Friday. Great for after work drinks, parties, corporate events etc.
I have attached our logo that I would like incorporated.
Our website is www.tamberlow.com.au if you would like to get a feel for the property.

Hotel

```html
<!DOCTYPE html>
<html lang="en">
<head>
<meta charset="utf-8">
<title>Tapas Friday – The Tamberlow</title>
<link href="https://fonts.googleapis.com/css2?family=Tenor+Sans&family=PT+Sans:wght@400;700&display=swap" rel="stylesheet">
<style>
  :root {
    --food-dark: #7a4a2a;
    --food-mid: #b8843e;
    --food-green: #7f8f45;
    --panel: #c4643c;
    --panel-deep: #a94e2c;
    --panel-light: #d98a5e;
    --gold: #f3dcae;
    --cream: #fff6ea;
    --badge: #e6743e;
    --logo-ink: #7a4b2e;
  }
  * { margin: 0; padding: 0; box-sizing: border-box; }
  html, body { width: 849px; height: 1200px; overflow: hidden; background: #fff; }
  .flyer {
    position: relative; width: 849px; height: 1200px; overflow: hidden;
    font-family: "PT Sans", Arial, sans-serif;
  }
  .food-backdrop {
    position: absolute; inset: 0;
    background:
      radial-gradient(circle at 15% 20%, var(--food-green) 0, transparent 22%),
      radial-gradient(circle at 85% 75%, var(--food-green) 0, transparent 20%),
      radial-gradient(circle at 80% 15%, #d9b47a 0, transparent 25%),
      linear-gradient(135deg, var(--food-mid), var(--food-dark) 50%, var(--food-mid));
  }
  .promo-panel {
    position: absolute; left: 51px; top: 51px; width: 747px; height: 1109px;
    background:
      radial-gradient(ellipse at 30% 25%, var(--panel-light) 0, transparent 45%),
      radial-gradient(ellipse at 70% 70%, var(--panel-deep) 0, transparent 50%),
      var(--panel);
    box-shadow: 0 0 0 2px rgba(255,230,200,.35);
  }
  .brand-tag {
    position: absolute; left: 306px; top: 0; width: 237px; height: 192px;
    background: #fff; display: flex; align-items: center; justify-content: center;
    box-shadow: 0 2px 8px rgba(0,0,0,.25);
  }
  .brand-name {
    font-family: "Tenor Sans", Georgia, sans-serif;
    color: var(--logo-ink); font-size: 30px; text-align: center; line-height: 1.15;
  }
  .dish-photo {
    position: absolute; left: 84px; top: 87px; width: 176px; height: 176px;
    border-radius: 50%; border: 4px solid #fff;
    background: radial-gradient(circle at 40% 40%, #e9d3a8, #a7763e 60%, #6e8a4a);
  }
  .wine-badge {
    position: absolute; left: 592px; top: 82px; width: 236px; height: 236px;
    border-radius: 50%; background: var(--badge);
    display: flex; flex-direction: column; align-items: center; justify-content: center;
    color: #fff; text-align: center;
  }
  .wine-badge .badge-title { font-weight: 700; font-size: 34px; line-height: 1.1; }
  .wine-badge .badge-hours { font-size: 25px; margin-top: 4px; }
  .headline {
    position: absolute; left: 51px; width: 747px; text-align: center;
    font-family: "Tenor Sans", Georgia, sans-serif; color: var(--gold);
    font-size: 178px; line-height: 1; letter-spacing: 2px;
  }
  .headline-tapas { top: 340px; }
  .headline-friday { top: 482px; }
  .occasions {
    position: absolute; left: 51px; width: 747px; top: 636px;
    text-align: center; color: var(--cream); font-size: 64px; line-height: 63px;
  }
  .contact { position: absolute; left: 51px; width: 747px; text-align: center; color: var(--cream); }
  .contact-address { top: 890px; font-size: 26px; }
  .contact-phone { top: 966px; font-size: 50px; }
  .contact-email { top: 1030px; font-size: 36px; }
</style>
</head>
<body>
  <div class="flyer">
    <div class="food-backdrop" role="img" aria-label="Photograph of assorted tapas dishes filling the background"></div>
    <div class="promo-panel"></div>
    <div class="dish-photo" role="img" aria-label="Round photograph of a plated tapas dish"></div>
    <div class="brand-tag"><span class="brand-name">The<br>Tamberlow</span></div>
    <div class="wine-badge">
      <div class="badge-title">OPEN WINE BAR</div>
      <div class="badge-hours">from 5pm to 8pm</div>
    </div>
    <div class="headline headline-tapas">TAPAS</div>
    <div class="headline headline-friday">FRIDAY</div>
    <div class="occasions">after work<br>drinks parties<br>corporate events</div>
    <div class="contact contact-address">14 Harlow Street, Bairnsdale, Victoria, 3875, Australia</div>
    <div class="contact contact-phone">+61 355550142</div>
    <div class="contact contact-email">info@tamberlow.com.au</div>
  </div>
</body>
</html>
```